Hochwertiges Plakat-Design für Konzert gesucht
Zielgruppe
Wir sind ein Konzertveranstalter und suchen ein hochwertiges Design für ein Konzertplakat. Unsere Zielgruppe sind Liebhaber der Filmmusik, eher Frauen im Alter 30+
Aufgabenstellung
Bei dem Projekt geht es um ein Konzertplakat - Format A0. Das Konzert hat den Titel GOLDEN CINEMA HEART SONGS, während des Konzertes wird die schönste und bekannteste Liebesmusik aus verschiedenen Filmen gespielt - live vom Aldric Ensemble in einer großen sinfonischen Besetzung.
GOLDEN CINEMA HEART SONGS
live mit dem Aldric Ensemble
Das Plakat soll auch die Namen der Komponisten - Piero Vasco, Mark Ellwood, Dario Fenzaletti, Peter Dalgley, Kurt Wessel - enthalten sowie separat einige Filmtitel: Unter Sternen entflohen, Tide Letter, Torvin und Elska, Meridor, Hinter dem Nebelberg, Velvet Stepping, Schatz der Nordsee, Bo Ri Vale.
Außerdem muss das Plakat auch die Informationen enthalten, wo und wann das Konzertstattfindet:
Freitag, 10.01.2020, Magdeburg, Kuppelsaal
sowie die Ticketinformationen:
Billettkiste im Brunnen-Passage, Ernst-Reuter Allee 11, 39104 Magdeburg
und an allen bekannten VVK-Stallen
Onlinetickets elbkartenwelt.de
Tickethotline: 0391-7482061
Die Informationen über das Datum und Ort sowie die Ticketinformationen müssen so gestaltet sein, dass man sie ersetzen kann, wenn das Konzert woanders stattfindet.

```html
<!DOCTYPE html>
<html lang="de">
<head>
<meta charset="utf-8">
<title>Golden Cinema Heart Songs – Konzertplakat</title>
<link rel="stylesheet" href="https://fonts.googleapis.com/css2?family=Bodoni+Moda:ital,wght@0,400;0,500;1,400&family=Great+Vibes&display=swap">
<style>
  :root {
    --night: #1f1f22;
    --night-deep: #121215;
    --neon-red: #b3271d;
    --neon-amber: #d9822b;
    --ink-light: #f4f1ec;
    --ink-soft: #e6e2dc;
    --shadow: rgba(0, 0, 0, 0.75);
  }
  * { box-sizing: border-box; margin: 0; padding: 0; }
  html, body {
    width: 851px;
    height: 1200px;
    overflow: hidden;
    background: var(--night);
  }
  .poster {
    position: relative;
    width: 851px;
    height: 1200px;
    overflow: hidden;
    background: var(--night);
    font-family: "Bodoni Moda", "Didot", serif;
    color: var(--ink-light);
  }
  .street-photo {
    position: absolute;
    inset: 0;
    background:
      radial-gradient(ellipse 140px 420px at 120px 520px, rgba(230, 60, 40, 0.55), transparent 70%),
      radial-gradient(ellipse 90px 300px at 40px 480px, rgba(217, 130, 43, 0.55), transparent 75%),
      radial-gradient(ellipse 120px 60px at 90px 790px, rgba(217, 150, 60, 0.35), transparent 80%),
      radial-gradient(circle 14px at 420px 345px, rgba(255, 255, 255, 0.8), transparent 100%),
      radial-gradient(ellipse 200px 240px at 480px 520px, rgba(90, 30, 30, 0.35), transparent 80%),
      linear-gradient(90deg, #3a1a17 0%, #2a1d1c 28%, var(--night) 45%, var(--night-deep) 100%);
  }
  .street-photo::after {
    content: "";
    position: absolute;
    inset: 0;
    background: linear-gradient(180deg, rgba(20,20,22,0.55) 0%, rgba(20,20,22,0) 30%, rgba(20,20,22,0) 60%, rgba(20,20,22,0.6) 100%);
  }
  .title {
    position: absolute;
    left: 0;
    right: 0;
    top: 58px;
    text-align: center;
    text-shadow: 3px 5px 8px var(--shadow);
  }
  .title-caps {
    display: block;
    font-weight: 400;
    font-size: 78px;
    line-height: 1;
    letter-spacing: -1px;
  }
  .title-script {
    display: block;
    font-family: "Great Vibes", cursive;
    font-size: 138px;
    line-height: 1;
    margin-top: 4px;
  }
  .performer {
    position: absolute;
    right: 72px;
    top: 330px;
    text-align: right;
    font-size: 32px;
    line-height: 1.3;
    color: var(--ink-soft);
    text-shadow: 2px 3px 6px var(--shadow);
  }
  .event-date {
    position: absolute;
    left: 0;
    right: 0;
    top: 806px;
    text-align: center;
    font-size: 36px;
    line-height: 1.35;
    padding-left: 20px;
    text-shadow: 2px 3px 6px var(--shadow);
  }
  .programme {
    position: absolute;
    left: 53px;
    right: 40px;
    top: 928px;
    font-size: 16.5px;
    line-height: 1.45;
    color: var(--ink-soft);
    text-shadow: 1px 2px 4px var(--shadow);
  }
  .tickets {
    position: absolute;
    left: 0;
    right: 0;
    top: 1040px;
    text-align: center;
    font-size: 16.5px;
    line-height: 1.65;
    padding-left: 20px;
    color: var(--ink-soft);
    text-shadow: 1px 2px 4px var(--shadow);
  }
</style>
</head>
<body>
<main class="poster">
  <div class="street-photo" role="img" aria-label="Nächtliche Straße mit rot leuchtender Kino-Neonfassade auf der linken Seite und einer Straßenlaterne im Dunkel"></div>

  <h1 class="title">
    <span class="title-caps">GOLDEN CINEMA</span>
    <span class="title-script">Heart Songs</span>
  </h1>

  <p class="performer">live mit dem<br>Aldric Ensemble</p>

  <p class="event-date">Freitag, 10.01.2020,<br>Magdeburg, Kuppelsaal</p>

  <p class="programme">Mit Musik von Piero Vasco, Mark Ellwood, Dario Fenzaletti, Peter Dalgley, Kurt Wessel.<br>Aus Filmen wie Unter Sternen entflohen, Tide Letter, Torvin und Elska, Meridor, Hinter dem Nebelberg, Velvet Stepping, Schatz der Nordsee, Bo Ri Vale</p>

  <p class="tickets">Billettkiste im Brunnen-Passage,<br>Lindwurmweg 27, 39112 Magdeburg<br>und an allen bekannten VVK-Stallen<br>Onlinetickets elbkartenwelt.de<br>Tickethotline: 0391-7482061</p>
</main>
</body>
</html>
```